Business Card Design Project

I have just chosen a logo and would now like this designed onto a business card for my hair salon. I would like it to be classy not to busy and have a wow factor when people look at them
Has to Include on card:
Logo Design
And business details below
Kellie-ann Drummond (owner)
0482 736 219
Rdw@vomblet.com.au
71 Willowmere Rise Corvin Cove
Logo is now attached please provide designs
Hair

```html
<!DOCTYPE html>
<html lang="en">
<head>
<meta charset="utf-8">
<title>Velora Hair Studio – Business Card</title>
<link rel="stylesheet" href="https://fonts.googleapis.com/css2?family=Arimo:wght@400;700&display=swap">
<style>
  :root {
    --backdrop: #2b2b2b;
    --card: #ffffff;
    --pink: #e8138a;
    --cyan: #5ec3d0;
    --ink: #1f1f1f;
    --divider: #2a2a2a;
  }
  * { margin: 0; padding: 0; box-sizing: border-box; }
  html, body {
    width: 1200px;
    height: 998px;
    overflow: hidden;
    background: var(--backdrop);
    font-family: "Arimo", Arial, sans-serif;
  }
  .card {
    position: absolute;
    left: 100px;
    top: 214px;
    width: 1000px;
    height: 570px;
    background: var(--card);
    border-radius: 44px;
    overflow: hidden;
    box-shadow: 0 18px 40px rgba(0,0,0,0.45);
  }
  .brand {
    position: absolute;
    left: 60px;
    top: 150px;
    width: 400px;
    height: 180px;
    display: flex;
    align-items: center;
    justify-content: center;
    gap: 16px;
  }
  .brand-mark {
    width: 22px;
    height: 22px;
    border-radius: 50%;
    background: var(--pink);
    flex: none;
  }
  .brand-name {
    color: var(--pink);
    font-weight: 700;
    font-size: 40px;
    line-height: 1.1;
    letter-spacing: 1px;
    text-transform: uppercase;
  }
  .divider {
    position: absolute;
    left: 505px;
    top: 70px;
    width: 2px;
    height: 330px;
    background: linear-gradient(to bottom, var(--divider) 0%, var(--divider) 75%, rgba(42,42,42,0) 100%);
  }
  .details {
    position: absolute;
    left: 548px;
    top: 62px;
    color: var(--ink);
  }
  .holder-name {
    color: var(--pink);
    font-weight: 700;
    font-size: 36px;
  }
  .holder-role {
    color: var(--cyan);
    font-size: 24px;
    margin-top: 6px;
  }
  .address {
    font-size: 24px;
    margin-top: 42px;
  }
  .contact-list {
    list-style: none;
    margin-top: 56px;
  }
  .contact-item {
    display: flex;
    align-items: center;
    gap: 14px;
    font-size: 24px;
    margin-bottom: 10px;
  }
  .contact-icon {
    width: 30px;
    height: 30px;
    flex: none;
  }
  .rule-cyan {
    position: absolute;
    left: 0;
    right: 0;
    bottom: 94px;
    height: 4px;
    background: var(--cyan);
  }
  .band-pink {
    position: absolute;
    left: 0;
    right: 0;
    bottom: 0;
    height: 86px;
    background: var(--pink);
  }
</style>
</head>
<body>
  <div class="card">
    <div class="brand">
      <span class="brand-mark"></span>
      <span class="brand-name">Velora<br>Hair Studio</span>
    </div>

    <div class="divider"></div>

    <div class="details">
      <p class="holder-name">Kellie-ann Drummond</p>
      <p class="holder-role">Owner</p>
      <p class="address">71 Willowmere Rise Corvin Cove</p>
      <ul class="contact-list">
        <li class="contact-item">
          <svg class="contact-icon" viewBox="0 0 30 30" aria-hidden="true">
            <path d="M4 11c0-4 5-6 11-6s11 2 11 6v2h-6v-3c-3-1-7-1-10 0v3H4z" fill="var(--pink)"/>
            <path d="M9 14h12l4 10H5z" fill="var(--pink)"/>
            <circle cx="15" cy="19" r="3" fill="#fff"/>
          </svg>
          <span>0482 736 219</span>
        </li>
        <li class="contact-item">
          <svg class="contact-icon" viewBox="0 0 30 30" aria-hidden="true">
            <rect x="4" y="8" width="22" height="15" fill="none" stroke="var(--pink)" stroke-width="2.5"/>
            <path d="M4 8l11 9 11-9" fill="none" stroke="var(--pink)" stroke-width="2.5"/>
          </svg>
          <span>Rdw@vomblet.com.au</span>
        </li>
      </ul>
    </div>

    <div class="rule-cyan"></div>
    <div class="band-pink"></div>
  </div>
</body>
</html>
```